We need a flyer where we promote a workshop to our members of the jewish community www.qvb-gemeinde.example . The workshop is calles "guidance in ten seasons presented by QVB. We would like to see a flyer with the below text is used and also some pictures (attached). The flyer should come over as cool, fresh, innovative for a younger crowd so called young professionals (age 28-35).
TITLE.
"Guidance in Ten Seasons.
SUBTITLE.
Your systematic self-coaching roadmap to power and impact—and your future.”
TEXT.
Dr. Martin K. Halvorsen is the CEO Emeritus of Alpine Advisory Partners—he made an exit in 2013. He is the award-winning author of 8 books, including "Plan-Into-Motion," "Speak or Falter" and "The Cantor and the Chairman.”
For the past 20 years he has taught leadership at Harwick University in New York and at BKU (Lindenberg University) to prepare future CEOs and other leaders in business, government , nonprofits and the military.
Now, in a process exclusively designed for QVB’s next generation of emerging leaders, Martin unpacks his leadership secrets in 3 action-packed labs—reduced to the max:
Lab 1. Guidance in Ten Seasons: The Summit Guide Triangle®. Self-Assessment. Self-Leadership: “The Lantern.” 5-Year Vision. 100-Day Catalytic Project.
Lab 2. Leading Through Language. Relationship: Building Trust. Plan-Into-Motion. Cockpit.
Lab 3. Debrief and Scale-Up. Sustainability. Action Tools.
Do you want to build your own future and a life you love? Do you want to jump-start that future and life over 100 days while learning a toolbox of leadership skills, networking with like-minded people—and even get some pizza? Then join us.
Target Market(s)
young professionals age 28-35

```html
<!DOCTYPE html>
<html lang="en">
<head>
<meta charset="utf-8">
<title>Guidance in Ten Seasons – QVB Workshop</title>
<link href="https://fonts.googleapis.com/css2?family=Inter:wght@800&family=Poppins:wght@400;700&family=Oswald:wght@500&display=swap" rel="stylesheet">
<style>
  :root {
    --brand-blue: #1656a8;
    --sky: #6ccbee;
    --ring: #1e90d6;
    --white: #ffffff;
    --photo-deep: #0c1a4a;
    --photo-mid: #2a4fb0;
  }
  * { margin: 0; padding: 0; box-sizing: border-box; }
  html, body { width: 849px; height: 1200px; overflow: hidden; }
  body { background: var(--brand-blue); font-family: "Poppins", sans-serif; color: var(--white); }
  .flyer { position: relative; width: 849px; height: 1200px; background: var(--brand-blue); overflow: hidden; }
  .hero { position: absolute; top: 0; left: 0; width: 849px; height: 520px; }
  .headline {
    position: absolute; left: 40px; top: 198px; z-index: 2;
    font-family: "Inter", sans-serif; font-weight: 800; color: var(--white);
  }
  .headline .line-1 { display: block; font-size: 80px; line-height: 84px; letter-spacing: 0.5px; }
  .headline .line-2 { display: block; font-size: 62px; line-height: 70px; letter-spacing: -1.5px; margin-top: -6px; white-space: nowrap; }
  .portrait {
    position: absolute; left: 489px; top: 267px; width: 334px; height: 334px; z-index: 1;
    border-radius: 50%; border: 12px solid var(--ring);
    background: radial-gradient(circle at 50% 38%, #e8e4e0 0%, #f4f4f4 45%, #5d6168 80%, #3e4249 100%);
  }
  .subtitle {
    position: absolute; left: 41px; top: 503px; width: 600px; z-index: 2;
    font-family: "Poppins", sans-serif; font-weight: 700; color: var(--sky);
    font-size: 38px; line-height: 45px; letter-spacing: -0.3px; white-space: nowrap;
  }
  .bio { position: absolute; left: 41px; top: 658px; width: 768px; font-size: 16px; line-height: 22.3px; text-align: justify; }
  .bio p + p { margin-top: 22px; }
  .lab {
    position: absolute; background: var(--sky); color: var(--brand-blue);
    border-radius: 20px; font-family: "Oswald", sans-serif; font-weight: 500;
    font-size: 17.5px; line-height: 32px; letter-spacing: -0.5px; padding: 6px 14px;
    white-space: nowrap;
  }
  .lab-1 { left: 26px; top: 891px; width: 394px; height: 145px; padding-top: 7px; }
  .lab-2 { left: 429px; top: 891px; width: 394px; height: 70px; padding-top: 3px; }
  .lab-3 { left: 429px; top: 968px; width: 394px; height: 69px; padding-top: 3px; }
  .invite { position: absolute; left: 41px; top: 1045px; width: 768px; font-size: 16px; line-height: 22.3px; text-align: justify; }
  .venue-band {
    position: absolute; left: 0; top: 1122px; width: 849px; height: 41px;
    background: var(--sky); color: var(--white);
    font-weight: 700; font-size: 16px; line-height: 41px; text-align: center;
  }
</style>
</head>
<body>
<main class="flyer">
  <svg class="hero" viewBox="0 0 849 520" width="849" height="520">
    <defs>
      <linearGradient id="stage-tone" x1="0" y1="0" x2="0" y2="1">
        <stop offset="0" stop-color="#0b0d1c"/>
        <stop offset="0.35" stop-color="#0c1a4a"/>
        <stop offset="1" stop-color="#2a4fb0"/>
      </linearGradient>
    </defs>
    <rect width="849" height="520" fill="url(#stage-tone)" role="img" aria-label="Photo of a speaker on a lit stage in front of a large seated audience"/>
    <path d="M0,352 C250,490 520,522 849,362 L849,520 L0,520 Z" fill="var(--brand-blue)"/>
    <path d="M0,352 C250,490 520,522 849,362" fill="none" stroke="var(--white)" stroke-width="5"/>
  </svg>

  <h1 class="headline"><span class="line-1">GUIDANCE</span><span class="line-2">in Ten Seasons</span></h1>

  <div class="portrait" role="img" aria-label="Portrait photo of Dr. Martin K. Halvorsen"></div>

  <h2 class="subtitle">Your systematic<br>self-coaching roadmap to<br>power, impact &amp; your future.</h2>

  <section class="bio">
    <p>Dr. Martin K. Halvorsen is the CEO Emeritus of Alpine Advisory Partners—he made an exit in 2013. He is the award-winning author of 8 books, including "Plan-Into-Motion," "Speak or Falter" and "The Cantor and the Chairman."</p>
    <p>For the past 20 years he has taught leadership at Harwick University in New York and at BKU (Lindenberg University) to prepare future CEOs and other leaders in business, government , non-profits and the military.</p>
    <p>Now, in a process exclusively designed for QVB’s next generation of emerging leaders, Martin unpacks his leadership secrets in 3 action-packed labs reduced to the max:</p>
  </section>

  <div class="lab lab-1">Lab 1. Guidance in Ten Seasons:<br>The Summit Guide Triangle®. Self-Assessment.<br>Self-Leadership: “The Lantern.” 5-Year Vision. 100-Day<br>Catalytic Project.</div>
  <div class="lab lab-2">Lab 2. Leading Through Language. Relationship:<br>Building Trust. Plan-Into-Motion. Cockpit.</div>
  <div class="lab lab-3">Lab 3. Debrief and Scale-Up. Sustainability. Action<br>Tools.</div>

  <p class="invite">Do you want to build your own future and a life you love? Do you want to jump-start that future and life over 100 days while learning a toolbox of leadership skills, networking with like-minded people and even get some pizza? Then join us.</p>

  <footer class="venue-band">QVB Gemeindezentrum, Lindenhofgasse 7, 8001 Zürich | +41 44 555 01 23</footer>
</main>
</body>
</html>
```